Business card to be used as a flyer

This business card should do the trick of a full scale flyer , so basicaly from the business card itself we only keep the size and remove the clasical name , position , company name (etc).
This business cards should be , like said above, used as promo tool, being gived to different girls . So base one : the design is girls oriented.
Colors : black background . We will use gold (color) folio for the text.
Attached you have our logo, but this should not be a proiminent part of the design . You can use only the cat head instead.
Target Market(s)
Girls / Women
Contact Information for Business Card
> black background , gold / folio text and elements
> cat head from the logo in a creative way do be displayed
> proieminent text "your path to success starts here"
> contact details phone and website .
www.velvadrome.ro (website) and 0741263519 (phone)
Font styles to use
Colors
Designer to choose only greyscale colors for use in the design.
Look and feel

```html
<!DOCTYPE html>
<html lang="en">
<head>
<meta charset="utf-8">
<title>Velvadrome – Promo Card</title>
<link href="https://fonts.googleapis.com/css2?family=Dancing+Script:wght@600&family=Roboto:wght@400&display=swap" rel="stylesheet">
<style>
  :root {
    --backdrop: #2b2b2b;
    --card-black: #0b0b0b;
    --card-edge: #1a1a1a;
    --gold: #d9a928;
    --gold-light: #f6d56a;
    --gold-deep: #a8781a;
  }
  * { margin: 0; padding: 0; box-sizing: border-box; }
  html, body {
    width: 1200px;
    height: 1108px;
    overflow: hidden;
    background: var(--backdrop);
  }
  .canvas {
    position: relative;
    width: 1200px;
    height: 1108px;
  }
  .card {
    position: absolute;
    top: 229px;
    width: 420px;
    height: 650px;
    border-radius: 18px;
    background: linear-gradient(160deg, var(--card-edge) 0%, var(--card-black) 55%, #050505 100%);
    overflow: hidden;
  }
  .card--front { left: 140px; }
  .card--back { left: 640px; }

  .brand-name {
    position: absolute;
    left: 0;
    right: 0;
    top: 282px;
    text-align: center;
    font-family: "Dancing Script", cursive;
    font-weight: 600;
    font-size: 52px;
    color: var(--gold);
  }

  .back-layout {
    position: absolute;
    width: 650px;
    height: 420px;
    left: -115px;
    top: 115px;
    transform: rotate(-90deg);
  }
  .tagline {
    position: absolute;
    left: 70px;
    top: 150px;
    font-family: "Dancing Script", cursive;
    font-weight: 600;
    font-size: 46px;
    white-space: nowrap;
    background: linear-gradient(90deg, var(--gold-deep), var(--gold-light) 45%, var(--gold) 70%, var(--gold-light));
    -webkit-background-clip: text;
    background-clip: text;
    color: transparent;
  }
  .contact-line {
    position: absolute;
    left: 110px;
    top: 258px;
    display: flex;
    align-items: center;
    gap: 8px;
    font-family: "Roboto", sans-serif;
    font-size: 15px;
    letter-spacing: 0.5px;
    color: var(--gold);
    white-space: nowrap;
  }
  .contact-line svg { width: 14px; height: 14px; }
  .contact-divider { margin: 0 6px; }
</style>
</head>
<body>
<main class="canvas">
  <section class="card card--front" aria-label="Card front">
    <div class="brand-name">Velvadrome</div>
  </section>

  <section class="card card--back" aria-label="Card back">
    <div class="back-layout">
      <p class="tagline">Your path to success starts here</p>
      <div class="contact-line">
        <svg viewBox="0 0 16 16" aria-hidden="true">
          <path fill="var(--gold)" d="M3.6 1.5l2.1 2.6-1.3 1.6c.8 1.9 2.1 3.3 4 4.2l1.6-1.3 2.6 2.1-1.2 2.4C6.3 12.7 3.3 9.7 1.2 3.7z"/>
        </svg>
        <span class="contact-phone">0741263519</span>
        <span class="contact-divider">|</span>
        <svg viewBox="0 0 16 16" aria-hidden="true">
          <g fill="none" stroke="var(--gold)" stroke-width="1.2">
            <circle cx="8" cy="8" r="6.5"/>
            <ellipse cx="8" cy="8" rx="2.8" ry="6.5"/>
            <line x1="1.5" y1="8" x2="14.5" y2="8"/>
          </g>
        </svg>
        <span class="contact-web">www.velvadrome.ro</span>
      </div>
    </div>
  </section>
</main>
</body>
</html>
```